Web Design Project for SEARCH ENGINE !

We need a website design for torrents search engine.

The Website will be www.Qurvex.com

Qurvex is a a search engine for torrents.
Qurvex search and index torrents results from all torrents sites.

We will need:
Logo
WebSite Design
slogen (optional)

we need only PSDs - no codded pages are needed !

Design to the following screen Size & resolution: 1024 x 768

***PLEASE DOWNLOAD ATTACHED FILE !

```html
<!DOCTYPE html>
<html lang="en">
<head>
<meta charset="utf-8">
<title>Qurvex – Torrent Meta-Search</title>
<link rel="stylesheet" href="https://fonts.googleapis.com/css2?family=Overpass:wght@500;600;700&family=Exo+2:ital,wght@1,900&display=swap">
<style>
  :root {
    --navy: #0f3168;
    --navy-deep: #0d2e63;
    --blue-edge: #1b68cc;
    --orange: #ff8706;
    --white: #ffffff;
    --placeholder: #d8d8d8;
    --rule: rgba(255,255,255,0.75);
  }
  html, body {
    margin: 0;
    padding: 0;
    overflow: hidden;
  }
  .page {
    position: relative;
    width: 1200px;
    height: 960px;
    overflow: hidden;
    background:
      radial-gradient(ellipse 62% 62% at 50% 45%, var(--navy-deep) 0%, var(--navy) 62%, var(--blue-edge) 100%);
    font-family: "Overpass", "Helvetica Neue", Arial, sans-serif;
    color: var(--white);
  }
  .site-header {
    position: absolute;
    left: 0;
    top: 0;
    width: 1200px;
    height: 128px;
    border-bottom: 1px solid var(--rule);
  }
  .brand {
    position: absolute;
    left: 117px;
    top: 52px;
    display: flex;
    align-items: center;
    gap: 8px;
    font-size: 46px;
    font-weight: 600;
    line-height: 1;
    color: var(--white);
    text-decoration: none;
  }
  .brand-dot {
    width: 11px;
    height: 11px;
    border-radius: 50%;
    background: var(--orange);
    margin-top: -22px;
  }
  .main-nav {
    position: absolute;
    top: 78px;
    left: 464px;
    display: flex;
    gap: 27px;
  }
  .nav-button {
    display: flex;
    align-items: center;
    justify-content: center;
    width: 163px;
    height: 49px;
    background: var(--orange);
    border-radius: 4px;
    color: var(--white);
    text-decoration: none;
    font-size: 24px;
    font-weight: 600;
    letter-spacing: 1.5px;
    padding-top: 6px;
    box-sizing: border-box;
  }
  .search-form {
    position: absolute;
    left: 246px;
    top: 352px;
    width: 786px;
    height: 85px;
    background: var(--orange);
    border-radius: 7px;
    display: flex;
    align-items: stretch;
  }
  .search-input {
    margin: 0 0 2px 5px;
    width: 545px;
    border: none;
    border-radius: 6px;
    background: var(--white);
    padding: 6px 0 0 22px;
    font-family: "Overpass", "Helvetica Neue", Arial, sans-serif;
    font-size: 38px;
    font-weight: 600;
    letter-spacing: 3px;
    color: #555;
    outline: none;
  }
  .search-input::placeholder {
    color: var(--placeholder);
  }
  .search-submit {
    flex: 1;
    border: none;
    background: transparent;
    color: var(--white);
    font-family: "Exo 2", "Arial Black", sans-serif;
    font-style: italic;
    font-weight: 900;
    font-size: 41px;
    letter-spacing: 0;
    padding: 0;
    cursor: pointer;
  }
  .tagline {
    position: absolute;
    left: 0;
    top: 566px;
    width: 1244px;
    margin: 0;
    text-align: center;
    font-size: 22px;
    font-weight: 600;
    line-height: 21px;
    letter-spacing: 2.4px;
  }
  .site-footer {
    position: absolute;
    left: 0;
    top: 887px;
    width: 1244px;
    text-align: center;
    font-size: 19px;
    font-weight: 600;
    letter-spacing: 1.6px;
  }
  .copyright-mark {
    font-size: 26px;
    font-weight: 500;
    vertical-align: -2px;
    margin-right: 6px;
  }
</style>
</head>
<body>
  <div class="page">
    <header class="site-header">
      <a class="brand" href="#"><span class="brand-dot"></span>Qurvex</a>
      <nav class="main-nav">
        <a class="nav-button" href="#">SEARCH</a>
        <a class="nav-button" href="#">PROFILE</a>
        <a class="nav-button" href="#">TORRENTS</a>
        <a class="nav-button" href="#">HELP</a>
      </nav>
    </header>

    <form class="search-form" action="#">
      <input class="search-input" type="text" placeholder="Enter Text Here" aria-label="Search torrents">
      <button class="search-submit" type="submit">SEARCH</button>
    </form>

    <p class="tagline">Qurvex is a free, fast and powerful meta-search engine<br>combining results from dozens of torrent search engines</p>

    <footer class="site-footer"><span class="copyright-mark">©</span>2011. All Rights Reserved. Qurvex</footer>
  </div>
</body>
</html>
```